Revamp a website that sells books on machine learning and A.I

Hello I would like to create a minimalist concept to revamp this website:

www.quillvane.co.uk

We can change everything including the logo.

Somethings that I don't like:
- Generic images of people.
- Robot images.

The books are about the mathematics for machine learning and A.I and I would like for the website to have a blog as well as a scheduling tool, were people can book a call with me.

The scheduling tool, needs to have text and different tiers, for example 15 m free and 60 m 45 usd

Target Market(s)

university students and mathematics enthusiasts

Industry/Entity Type

machine learning, education, books, mathematics, A.I

Number of Pages Required

4 page

Requirements
Must have
• Landing Page, blog page, scheduling page, optimised conversion funnel
Should not have
• Arbitrary images from people or robots

```html
<!DOCTYPE html>
<html lang="en">
<head>
<meta charset="utf-8">
<title>Quillvane – The Math Behind AI</title>
<link href="https://fonts.googleapis.com/css2?family=Alegreya+Sans:wght@500;700;800&family=Poppins:wght@400;500;600&display=swap" rel="stylesheet">
<style>
:root{
  --green:#27804f;
  --yellow:#f2b63c;
  --orange:#f6a21a;
  --red:#e04b3f;
  --cream:#faf4e4;
  --ink:#1c1c1c;
  --dark:#1f1f1f;
  --line:#e7e2d6;
}
*{box-sizing:border-box;margin:0;padding:0}
html,body{width:1200px;height:4762px;overflow:hidden}
body{font-family:"Poppins",sans-serif;color:var(--ink);background:#fff;position:relative}
.abs{position:absolute}
.head{font-family:"Alegreya Sans",sans-serif;font-weight:800;line-height:1.05}
.btn{display:inline-flex;align-items:center;justify-content:center;font-family:"Poppins",sans-serif;font-weight:600;font-size:11px;letter-spacing:.3px;text-transform:uppercase;text-decoration:none}
.rule{position:absolute;height:3px;width:150px;background:var(--orange);left:525px}
.stars{color:var(--yellow);letter-spacing:2px}

/* hero */
.hero{position:absolute;top:0;left:0;width:1200px;height:625px;background:linear-gradient(120deg,#fbf3dc 0%,#fbf6e7 50%,#f8efd5 100%);overflow:hidden}
.logo{font-family:"Alegreya Sans",sans-serif;font-weight:800;font-size:36px;color:var(--yellow);letter-spacing:.5px}
.nav{position:absolute;top:38px;left:383px;display:flex;gap:44px;font-size:11px;font-weight:500}
.hero-line{position:absolute;top:92px;left:140px;width:920px;height:1px;background:#e6dcbf}
.hero h1{position:absolute;left:140px;top:226px;font-size:62px;text-transform:uppercase}
.hero h1 .y{color:var(--yellow)} .hero h1 .g{color:var(--green)}
.cover{background:linear-gradient(160deg,#f5c75a,#e9b03e)}
.deco{position:absolute;font-family:"Poppins",sans-serif;font-weight:600;line-height:1}

/* books */
.sec-title{position:absolute;left:0;width:1200px;text-align:center;text-transform:uppercase;font-size:46px}
.card{position:absolute;top:882px;width:340px;height:638px;border:1px solid #8cbfa2;background:#fff}
.card .art{position:absolute;top:0;left:0;width:100%;height:431px;background:var(--green)}
.card .bk{position:absolute;left:68px;top:46px;width:206px;height:354px;box-shadow:0 3px 10px rgba(0,0,0,.25)}
.card .title{position:absolute;top:450px;left:0;width:100%;text-align:center;font-size:17px;font-weight:600;line-height:1.3}
.card .sep{position:absolute;top:515px;left:90px;width:160px;height:1px;background:var(--line)}
.card .stars{position:absolute;top:502px;left:0;width:100%;text-align:center;font-size:20px;line-height:1.2}
.card .price{position:absolute;top:540px;left:0;width:100%;text-align:center;font-weight:600;font-size:18px}
.card .btn{position:absolute;top:578px;left:98px;width:144px;height:33px;color:#fff;font-size:9px}

/* about */
.about{position:absolute;top:1614px;left:0;width:1200px;height:675px;background:var(--cream)}
.about p{font-size:12.5px;line-height:22.5px;color:#444}

/* testimonials */
.tcard{position:absolute;top:2598px;width:224px;height:296px;background:#fff;border:1px solid #eee;box-shadow:0 4px 14px rgba(0,0,0,.06);text-align:center}
.tcard .av{position:absolute;top:-37px;left:75px;width:74px;height:70px;border:2px solid var(--green);background:linear-gradient(#e9e4dc,#c9b9a4)}
.tcard p{position:absolute;top:60px;left:22px;right:22px;font-size:10.5px;line-height:19px;color:#555}
.tcard .stars{position:absolute;top:210px;width:100%;font-size:11px}
.tcard .nm{position:absolute;top:228px;width:100%;font-family:"Alegreya Sans",sans-serif;font-weight:700;color:var(--green);font-size:15px}
.tcard .loc{position:absolute;top:250px;width:100%;font-size:9.5px;color:#999}
.arrow{position:absolute;top:2720px;width:40px;height:36px;border:2px solid var(--ink);display:flex;align-items:center;justify-content:center;background:#fff}

/* consult */
.consult{position:absolute;top:3029px;left:0;width:1200px;height:553px;background:var(--green);overflow:hidden}
.tier{position:absolute;top:284px;width:344px;height:176px;background:var(--cream);text-align:center}
.tier h4{margin-top:30px;font-size:18px;font-weight:600}
.tier .pr{margin-top:10px;color:var(--red);font-weight:600;font-size:18px}
.tier .btn{margin-top:14px;height:36px;padding:0 16px;background:var(--orange);color:#fff;font-size:9px}

/* blog */
.bcard{position:absolute;top:3831px;width:228px;height:322px;background:#fff;box-shadow:0 4px 14px rgba(0,0,0,.08)}
.bcard .img{height:135px;background:linear-gradient(135deg,#d8d3cb,#8e8174)}
.bcard .date{position:absolute;top:124px;left:18px;background:var(--yellow);color:#fff;font-size:10px;padding:4px 14px}
.bcard h5{position:absolute;top:157px;left:20px;font-size:15px;font-weight:600}
.bcard p{position:absolute;top:185px;left:20px;right:16px;font-size:10px;line-height:17px;color:#555}
.bcard .btn{position:absolute;top:280px;left:6px;width:216px;height:32px;border:1px solid #eee;color:var(--ink);font-size:9px}

/* footer */
.footer{position:absolute;top:4247px;left:0;width:1200px;height:515px;background:var(--dark);color:#fff}
.fnav{position:absolute;top:362px;left:0;width:100%;display:flex;justify-content:center;gap:46px;font-size:10.5px;font-weight:500}
.sq{width:30px;height:30px;border:1px solid #666;display:flex;align-items:center;justify-content:center}
.sq span{width:8px;height:8px;background:#fff;border-radius:50%}
</style>
</head>
<body>

<section class="hero">
  <div class="abs logo" style="left:140px;top:26px">QUILLVANE</div>
  <nav class="nav"><span>HOME</span><span>ABOUT US</span><span>BOOKS</span><span>BLOG</span><span>CONTACT</span></nav>
  <div class="abs" style="left:832px;top:40px;font-size:11px;font-weight:500">LOG IN</div>
  <svg class="abs" style="left:888px;top:34px" width="26" height="24" viewBox="0 0 26 24"><path d="M2 4h4l3 11h11l3-8H8" fill="none" stroke="var(--orange)" stroke-width="2.2"/><circle cx="11" cy="19" r="2" fill="var(--orange)"/><circle cx="19" cy="19" r="2" fill="var(--orange)"/><circle cx="21" cy="5" r="5" fill="var(--green)"/></svg>
  <a class="btn abs" style="left:928px;top:32px;width:132px;height:32px;background:var(--green);color:#fff;font-size:9.5px">Schedule a call</a>
  <div class="hero-line"></div>
  <h1 class="head">The <span class="y">Math</span> Behind<br><span class="g">AI</span> Starts Here</h1>
  <div class="abs" style="left:140px;top:368px;font-size:12px;font-weight:500">EXPLORE OUR COLLECTION OF BOOKS ON MATHEMATICS FOR ML AND A.I.</div>
  <a class="btn abs" style="left:140px;top:414px;width:164px;height:41px;background:var(--green);color:#fff">Browse books</a>
  <a class="btn abs" style="left:312px;top:414px;width:187px;height:41px;border:2px solid var(--green);color:var(--ink)">Start with a free call</a>
  <div class="abs cover" role="img" aria-label="Illustrated cover of the calculus volume, tilted with a second copy behind" style="left:730px;top:150px;width:270px;height:370px;transform:rotate(16deg);box-shadow:-10px 8px 0 #e3a73a,0 10px 24px rgba(0,0,0,.25)"></div>
  <div class="deco" style="left:1068px;top:200px;color:var(--orange);font-size:34px">×</div>
  <div class="deco" style="left:1022px;top:418px;color:var(--red);font-size:36px">+</div>
  <div class="deco" style="left:675px;top:510px;color:var(--green);font-size:32px">×</div>
  <div class="deco" style="left:712px;top:258px;color:var(--orange);font-size:30px">÷</div>
  <div class="abs" style="left:908px;top:136px;width:24px;height:4px;background:var(--red)"></div>
</section>

<h2 class="sec-title head" style="top:716px"><span style="color:var(--yellow)">Explore our</span><br>Best-selling books</h2>
<div class="rule" style="top:835px"></div>

<article class="card" style="left:235px">
  <div class="art"><div class="bk cover" role="img" aria-label="Illustrated cover, volume 2 – calculus"></div></div>
  <svg class="abs" style="left:0;top:0" width="84" height="84"><path d="M0 0h84L0 84z" fill="#fff"/><text x="8" y="44" transform="rotate(-45 30 30)" font-family="Poppins" font-size="8" font-weight="600">LATEST RELEASE</text></svg>
  <div class="title">BENEATH THE MODEL<br>VOL 2 - CALCULUS</div>
  <div class="sep"></div>
  <div class="stars">★★★★★</div>
  <div class="price">7,50 €</div>
  <a class="btn" style="background:var(--orange)">Add to cart</a>
</article>
<article class="card" style="left:625px;background:var(--cream);box-shadow:0 8px 20px rgba(0,0,0,.12)">
  <div class="art"><div class="bk cover" role="img" aria-label="Illustrated cover, volume 1 – linear algebra"></div></div>
  <div class="title">BENEATH THE MODEL<br>VOL 1 - LINEAR ALGEBRA</div>
  <div class="sep"></div>
  <div class="stars">★★★★★</div>
  <div class="price">7,50 €</div>
  <a class="btn" style="background:var(--red)">Add to cart</a>
</article>

<section class="about">
  <div class="abs" style="left:860px;top:0;width:200px;height:675px;background:var(--green)"></div>
  <div class="abs" role="img" aria-label="Portrait photo of the author" style="left:647px;top:109px;width:343px;height:485px;background:linear-gradient(150deg,#c9b58e,#6d4e36 60%,#3b2a1f)"></div>
  <div class="abs head" style="left:234px;top:114px;font-size:44px;text-transform:uppercase"><span style="color:var(--yellow)">Hello!</span><br>I am Luis Prado</div>
  <div class="abs" style="left:234px;top:240px;width:126px;height:3px;background:var(--orange)"></div>
  <div class="abs" style="left:234px;top:272px;font-size:11px;font-weight:600">A MATHEMATICIAN AND NOW A BOOK WRITER</div>
  <p class="abs" style="left:234px;top:300px;width:372px">I am a mathematician with over a decade of experience in developing &amp; deploying machine learning systems. My books are written in an conversational style with humour. They are rich in practical applications, enabling readers to not only grasp the concepts but also understand their real-world applications in the field of Data Science.</p>
  <a class="btn abs" style="left:234px;top:463px;width:138px;height:36px;background:var(--red);color:#fff;font-size:9.5px">Schedule a call</a>
  <div class="abs" style="left:234px;top:540px;font-size:9.5px;font-weight:600">FOLLOW US -</div>
  <div class="abs" style="left:234px;top:568px;display:flex;gap:22px">
    <span style="width:9px;height:9px;border-radius:50%;background:#333"></span><span style="width:9px;height:9px;border-radius:50%;background:#333"></span><span style="width:9px;height:9px;border-radius:50%;background:#333"></span><span style="width:9px;height:9px;border-radius:50%;background:#333"></span>
  </div>
  <div class="deco" style="left:54px;top:70px;color:#e8d9b6;font-size:30px">÷</div>
  <div class="deco" style="left:786px;top:70px;color:#e8d9b6;font-size:30px">×</div>
  <div class="deco" style="left:1100px;top:320px;color:#e8d9b6;font-size:30px">+</div>
  <div class="deco" style="left:126px;top:470px;color:#e1e1e1;font-size:30px">×</div>
</section>

<h2 class="sec-title head" style="top:2372px;text-transform:none"><span style="color:var(--yellow)">What Our</span><br>Readers Are Saying</h2>
<div class="rule" style="top:2490px"></div>
<div class="arrow" style="left:140px"><svg width="20" height="14"><path d="M19 7H2M8 1L2 7l6 6" fill="none" stroke="var(--red)" stroke-width="2"/></svg></div>
<div class="arrow" style="left:1020px"><svg width="20" height="14"><path d="M1 7h17M12 1l6 6-6 6" fill="none" stroke="var(--red)" stroke-width="2"/></svg></div>
<div class="tcard" style="left:235px"><div class="av" role="img" aria-label="Reader avatar"></div><p>"As a student going into ML without much of a linear algebra foundation, I'm finding this book highly useful. Starts form the basics and works at a reasonable pace to establish core ML concepts..."</p><div class="stars">★★★★★</div><div class="nm">- Rowan</div><div class="loc">Catalonia, Spain</div></div>
<div class="tcard" style="left:488px"><div class="av" role="img" aria-label="Reader avatar"></div><p>" If you are looking for a resource that elegantly combines breadth and depth such you can understand the fundamentals of linear algebra to ultimately apply them to your ML projects, this is your stop."</p><div class="stars">★★★★★</div><div class="nm">- Elliot Marsh</div><div class="loc">Catalonia, Spain</div></div>
<div class="tcard" style="left:741px"><div class="av" role="img" aria-label="Reader avatar"></div><p>"The conversational tone of the book is its biggest strength. It feels less like a traditional text book and more like a novel. This approach makes the reader feel at ease, particularly when tackling complex topics."</p><div class="stars">★★★★★</div><div class="nm">- Noor</div><div class="loc">Catalonia, Spain</div></div>
<div class="abs" style="left:552px;top:2931px;display:flex;gap:5px">
  <span style="width:16px;height:3px;background:#ccc"></span><span style="width:16px;height:3px;background:var(--red)"></span><span style="width:16px;height:3px;background:#ccc"></span><span style="width:16px;height:3px;background:#ccc"></span><span style="width:16px;height:3px;background:#ccc"></span>
</div>

<section class="consult">
  <div class="abs" style="left:-120px;top:-60px;width:420px;height:260px;background:rgba(255,255,255,.05);transform:rotate(-35deg)"></div>
  <div class="abs" style="left:1000px;top:80px;width:320px;height:220px;background:rgba(255,255,255,.06);transform:rotate(-35deg)"></div>
  <h2 class="abs head" style="left:0;top:95px;width:1200px;text-align:center;color:#fff;font-size:46px">Book Your Consultation</h2>
  <div class="abs" style="left:525px;top:166px;width:150px;height:3px;background:#fff"></div>
  <p class="abs" style="left:0;top:198px;width:1200px;text-align:center;color:#fff;font-size:11px;line-height:22px">Whether you're just getting started or looking to dive deeper into advanced concepts,<br>schedule a one-on-one session for expert advice on understanding the math behind machine learning and AI.<br>Choose the option that best suits your needs.</p>
  <div class="tier" style="left:235px"><h4>15-MINUTE SESSION</h4><div class="pr">FREE</div><a class="btn">Schedule a free call</a></div>
  <div class="tier" style="left:621px"><h4>60-MINUTE SESSION</h4><div class="pr">$45 USD</div><a class="btn">Book a 60-minute session</a></div>
  <div class="deco" style="left:130px;top:100px;color:rgba(255,255,255,.25);font-size:30px">÷</div>
  <div class="deco" style="left:1000px;top:215px;color:rgba(255,255,255,.25);font-size:30px">×</div>
  <div class="deco" style="left:168px;top:330px;color:rgba(255,255,255,.25);font-size:30px">×</div>
  <div class="deco" style="left:1025px;top:400px;color:rgba(255,255,255,.25);font-size:30px">+</div>
</section>

<h2 class="sec-title head" style="top:3672px;text-transform:none"><span style="color:var(--yellow)">Deepen Your Understanding</span><br>with Our Blog</h2>
<div class="rule" style="top:3792px"></div>
<article class="bcard" style="left:235px"><div class="img" role="img" aria-label="Photo of an open book and phone"></div><span class="date">02-09-2024</span><h5>Tittle name will here...</h5><p>Lorem ipsum dolor sit amet, enim consectetur adipiscing elit. Etiam rutrum enim sit amet lacus molestie, vitae semper nisl imperdiet.</p><a class="btn">Learn more</a></article>
<article class="bcard" style="left:486px"><div class="img" role="img" aria-label="Photo of a tablet and coffee on a desk"></div><span class="date">02-09-2024</span><h5>Tittle name will here...</h5><p>Lorem ipsum dolor sit amet, enim consectetur adipiscing elit. Etiam rutrum enim sit amet lacus molestie, vitae semper nisl imperdiet.</p><a class="btn" style="background:var(--red);color:#fff;border:none">Learn more</a></article>
<article class="bcard" style="left:737px"><div class="img" role="img" aria-label="Photo of a reader in a library"></div><span class="date">02-09-2024</span><h5>Tittle name will here...</h5><p>Lorem ipsum dolor sit amet, enim consectetur adipiscing elit. Etiam rutrum enim sit amet lacus molestie, vitae semper nisl imperdiet.</p><a class="btn">Learn more</a></article>

<footer class="footer">
  <div class="abs head" style="left:140px;top:76px;font-size:31px;text-transform:uppercase;line-height:1.1">Subscribe<br>for a free chapter!</div>
  <div class="abs" style="left:653px;top:84px;width:407px;height:50px;border:1px solid #555;display:flex;align-items:center;justify-content:space-between;padding:0 6px 0 24px">
    <span style="font-size:10px;color:#aaa">Enter email address...</span>
    <span class="btn" style="background:#fff;color:var(--ink);height:36px;width:108px;font-size:10px">Subscribe</span>
  </div>
  <div class="abs" style="left:140px;top:176px;width:920px;height:1px;background:#3a3a3a"></div>
  <div class="abs logo" style="left:0;top:222px;width:1200px;text-align:center">QUILLVANE</div>
  <div class="abs" style="left:527px;top:282px;display:flex;gap:7px"><div class="sq"><span></span></div><div class="sq"><span></span></div><div class="sq"><span></span></div><div class="sq"><span></span></div></div>
  <div class="fnav"><span>HOME</span><span>ABOUT US</span><span>BOOKS</span><span>BLOG</span><span>CONTACT</span></div>
  <div class="abs" style="left:140px;top:458px;width:920px;height:1px;background:#3a3a3a"></div>
  <div class="abs" style="left:0;top:483px;width:1200px;text-align:center;font-size:10px;color:#ccc">Copyright © 2024 All rights reserved by Quillvane</div>
</footer>

</body>
</html>
```